Bluegate Wound Care and Hyperbarics Website Refresh

I want to revamp my current website to be more streamlined and look cleaner. I am also adding additional service lines and another location to the company so I would like that added as well. I want to stick with the same logo and colors, but just have it cleaned up with a better overall design.

www.bghyperbarics-example.com

Target Market(s)

Wound Care and Hyperbaric Patients

Industry/Entity Type

Healthcare

Coding

Coded - Design and coding required

Number of Pages Required

5+ page

Colors
0054AA
0677BA
7BADD7
CADEEF
E8F1F8
59FF00
82FF00
B8FF75
E3FFCB
F4FFEA

```html
<!DOCTYPE html>
<html lang="en">
<head>
<meta charset="utf-8">
<title>Bluegate Wound Care &amp; Hyperbarics</title>
<link href="https://fonts.googleapis.com/css2?family=Poppins:wght@400;500;600;700&family=Roboto:wght@300;400;500;700&display=swap" rel="stylesheet">
<style>
:root{
  --blue:#0054AA;
  --blue-mid:#0677BA;
  --green:#76B82A;
  --ink:#111111;
  --text:#444444;
  --muted:#888888;
  --line:#cfcfcf;
  --pale:#E8F1F8;
  --footer:#1f2833;
}
*{box-sizing:border-box;margin:0;padding:0}
html,body{width:1200px;height:3534px;overflow:hidden}
body{position:relative;font-family:'Roboto',sans-serif;color:var(--text);background:#fff}
.abs{position:absolute}
h1,h2,h3,h4,.poppins{font-family:'Poppins',sans-serif}

/* header */
.site-header{top:0;left:0;width:1200px;height:85px;background:#fff}
.brand{display:flex;align-items:center;gap:10px;font-family:'Poppins',sans-serif;font-weight:600;font-size:36px;color:var(--ink);letter-spacing:1px}
.brand .dot{width:30px;height:30px;border-radius:50%;background:var(--green)}
.header-brand{left:85px;top:18px}
.contact-item{display:flex;gap:8px;font-size:13px;line-height:20px;color:#555}
.contact-item b{color:#111;font-weight:500}
.contact-item svg{flex:none;margin-top:4px}
.main-nav{top:85px;left:0;width:1200px;height:49px;background:var(--green)}
.nav-links{left:85px;top:0;height:49px;display:flex;align-items:center;gap:22px;color:#fff;font-size:14px;font-weight:500;font-family:'Poppins',sans-serif}
.social{display:flex;gap:10px}
.social span{width:22px;height:22px;background:rgba(255,255,255,.35);border-radius:3px;display:block}
.btn{display:inline-flex;align-items:center;justify-content:center;background:var(--blue);color:#fff;font-family:'Poppins',sans-serif;font-size:13px;font-weight:500;text-transform:uppercase}

/* hero */
.hero{top:134px;left:0;width:1200px;height:608px;background:linear-gradient(180deg,#dfe9ef 0%,#eef3f6 55%,#dde6ec 100%);text-align:center}
.hero-kicker{position:absolute;top:170px;width:100%;font-family:'Poppins',sans-serif;font-size:19px;color:#222}
.hero-title{position:absolute;top:209px;left:191px;width:815px;height:62px;background:var(--green);font-size:57px;font-weight:700;line-height:62px;color:#111;letter-spacing:-.3px;white-space:nowrap}
.hero-copy{position:absolute;top:303px;left:300px;width:600px;font-size:15px;line-height:23px;color:#222}

/* contact */
.section-title{font-family:'Poppins',sans-serif;font-weight:600;color:var(--ink)}
.rule{width:57px;height:2px;background:#111}
.field{position:absolute;border:1px solid var(--line);background:#fff;font-size:13px;color:#888;padding:0 16px;display:flex;align-items:center}

/* about band */
.about{top:1327px;left:0;width:1200px;height:462px;background:linear-gradient(180deg,#3b3d40,#2b2d30);text-align:center;color:#fff}
.about p{font-size:14px;line-height:21px;width:830px;margin:0 auto 12px}

/* team */
.team-card{position:absolute;top:1941px;width:502px;height:200px;background:#fff;box-shadow:0 2px 14px rgba(0,0,0,.08);display:flex}
.team-card .ph{width:223px;height:200px;flex:none}
.team-card .body{padding:26px 26px 0}
.team-card h4{color:var(--blue);font-size:18px;font-weight:600}
.team-card .role{color:#999;font-size:13px;margin:4px 0 14px}
.team-card p{color:#777;font-size:12.5px;line-height:19px}

/* cta */
.cta{top:2225px;left:0;width:1200px;height:126px;background:#000;color:#fff}

/* news */
.news-card{position:absolute;top:2516px;width:325px;height:504px;border:1px solid #ddd;background:#fff}
.news-card .ph{height:212px;border-bottom:5px solid var(--green)}
.news-card .body{padding:30px 28px 0}
.news-card h4{font-size:15.5px;line-height:23px;font-weight:600;color:#111}
.news-card .meta{font-size:11px;color:var(--blue);margin:9px 0 22px}
.news-card p{font-size:13.5px;line-height:21px;color:#888}
.news-card .more{margin-top:16px;font-size:14px;color:var(--blue);font-weight:500;display:flex;align-items:center;gap:6px}

/* footer */
.site-footer{top:3105px;left:0;width:1200px;height:429px;background:linear-gradient(180deg,#27303b,#1a2129);color:#fff}
.site-footer h4{font-size:18px;font-weight:600;margin-bottom:18px}
.foot-list{list-style:none;font-size:14px}
.foot-list li{display:flex;gap:10px;margin-bottom:17px;line-height:20px}
.foot-list li::before{content:"›";font-size:17px;line-height:19px}
.foot-list b{font-weight:500}
.contact-list li{margin-bottom:12px}
</style>
</head>
<body>

<header class="abs site-header">
  <div class="abs header-brand brand"><span class="dot"></span>BLUEGATE</div>
  <div class="abs contact-item" style="left:750px;top:24px">
    <svg width="14" height="14" viewBox="0 0 24 24"><path fill="#76B82A" d="M6.6 10.8a15 15 0 006.6 6.6l2.2-2.2c.3-.3.7-.4 1-.2 1.1.4 2.3.6 3.6.6.6 0 1 .4 1 1V20c0 .6-.4 1-1 1A17 17 0 013 4c0-.6.4-1 1-1h3.5c.6 0 1 .4 1 1 0 1.3.2 2.5.6 3.6.1.3 0 .7-.2 1z"/></svg>
    <div>Phone No:<br><b style="font-weight:700">555-014-2290</b></div>
  </div>
  <div class="abs contact-item" style="left:900px;top:22px">
    <svg width="12" height="16" viewBox="0 0 12 16"><path fill="#76B82A" d="M6 0a6 6 0 016 6c0 4.5-6 10-6 10S0 10.5 0 6a6 6 0 016-6zm0 3.5a2.5 2.5 0 100 5 2.5 2.5 0 000-5z"/></svg>
    <div>Locations: <b>Fairview, TX</b><br><b>&amp; Westbrook, TX (New)</b></div>
  </div>
</header>

<nav class="abs main-nav">
  <div class="abs nav-links">
    <span>HOME</span><span>|</span><span>ABOUT</span><span>|</span><span>BLOG</span><span>|</span><span>CONTACT US</span>
  </div>
  <div class="abs social" style="left:847px;top:13px"><span></span><span></span><span></span><span></span></div>
  <div class="abs btn" style="left:987px;top:0;width:128px;height:49px">Learn More</div>
</nav>

<section class="abs hero" role="img" aria-label="Blurred photo of a hyperbaric oxygen chamber in a bright clinic room">
  <div class="hero-kicker">State of the Art Wound Care</div>
  <h1 class="hero-title">Hyperbaric Oxygen Therapy</h1>
  <p class="hero-copy">Bluegate Wound Care &amp; Hyperbarics is dedicated to the highest level of service with state of the art science for wound care. We are committed to our patient’s overall wellbeing and health.</p>
  <div class="btn" style="position:absolute;left:535px;top:390px;width:128px;height:49px">Learn More</div>
</section>

<section class="abs" style="top:742px;left:0;width:1200px;height:585px">
  <h2 class="abs section-title" style="left:85px;top:72px;font-size:38px">Contact Us!</h2>
  <div class="abs" style="left:85px;top:128px;font-size:13px;color:#555">Let us show you the Bluegate Wound Care Difference!</div>
  <div class="abs rule" style="left:85px;top:159px"></div>
  <div class="field" style="left:85px;top:190px;width:283px;height:43px">First Name *</div>
  <div class="field" style="left:392px;top:190px;width:283px;height:43px">Last Name *</div>
  <div class="field" style="left:85px;top:251px;width:283px;height:42px">Email *</div>
  <div class="field" style="left:392px;top:251px;width:283px;height:42px">Phone No. *</div>
  <div class="field" style="left:85px;top:311px;width:590px;height:122px;align-items:flex-start;padding-top:14px;padding-left:20px">How can we help? *</div>
  <div class="abs btn" style="left:86px;top:460px;width:136px;height:42px">Submit</div>
  <div class="abs" role="img" aria-label="Photo of a doctor in a white coat with a stethoscope, arms crossed" style="left:733px;top:37px;width:350px;height:548px;background:linear-gradient(180deg,#d9d4cf 0%,#eef0f2 40%,#f3f4f6 100%);border-radius:160px 160px 0 0"></div>
</section>

<section class="abs about" role="img" aria-label="Dark photo of hyperbaric chambers in a treatment room">
  <h2 class="poppins" style="margin-top:72px;font-size:38px;font-weight:600">Wound Care at Bluegate</h2>
  <div style="font-size:14px;margin-top:2px">About Bluegate Wound Care &amp; Hyperbarics</div>
  <div style="width:57px;height:2px;background:#fff;margin:12px auto 26px"></div>
  <p>At Bluegate Wound Care &amp; Hyperbarics we are committed to the highest level of care with state of the art technology in our hyperbaric oxygen therapy clinics. Our stand-alone clinics offer hyperbaric medicine in a conveniently located, outpatient setting.</p>
  <p>Hyperbaric oxygen therapy (HBOT) for wound care is considered the preferred modality for many patients who are at risk with delayed wound healing. Wounds need oxygen to heal properly and exposing a wound to 100% oxygen can speed healing and shorten recovery time. HBOT has also proven to be effective treating hearing issues, chronic ulcers, burn victims, injuries from radiation, migraines and some types of cancer.</p>
  <p>Our services now include advanced wound care, HBOT, diabetic foot care, lymphedema therapy and ostomy care, offered at two locations: Fairview and our new Westbrook clinic. Let us show you the difference today.</p>
</section>

<section class="abs" style="top:1789px;left:0;width:1200px;height:436px">
  <h2 class="abs section-title" style="left:85px;top:73px;font-size:38px">Meet Our Team</h2>
  <div class="abs rule" style="left:85px;top:134px"></div>
</section>
<article class="team-card" style="left:85px">
  <div class="ph" role="img" aria-label="Photo of the chief executive officer in a blue suit" style="background:linear-gradient(180deg,#e6e6e6,#c9ccd2)"></div>
  <div class="body"><h4>Daniel R. Moreau</h4><div class="role">Chief Executive Officer</div><p>Realizing the need for underutilized ancillary healthcare services like hyperbaric therapy, Daniel founded Bluegate Wound Care and Hyperbarics.</p></div>
</article>
<article class="team-card" style="left:613px">
  <div class="ph" role="img" aria-label="Photo of a patient inside a hyperbaric chamber" style="background:linear-gradient(180deg,#d8dbe0,#b9bec6)"></div>
  <div class="body"><h4>Your Provider</h4><div class="role">Board-Certified Nurse Practioner</div><p>At Bluegate, you will be treated by a highly-skilled provider, specially trained in wound care &amp; hyperbaric medicine.</p></div>
</article>

<section class="abs cta">
  <h2 class="abs poppins" style="left:85px;top:26px;font-size:36px;font-weight:600">Learn More Today!</h2>
  <div class="abs" style="left:85px;top:80px;font-size:13px">Give us a call to schedule a consult.</div>
  <div class="abs poppins" style="left:587px;top:47px;display:flex;align-items:center;gap:18px;font-size:21px;font-weight:600">
    <svg width="24" height="20" viewBox="0 0 24 20"><path fill="#fff" d="M2 6C2 2 22 2 22 6v2h-5V6H7v2H2zM6 9h12l3 10H3zm6 3a2.5 2.5 0 100 5 2.5 2.5 0 000-5z"/></svg>Call: 555-014-2290</div>
  <div class="abs poppins" style="left:870px;top:47px;display:flex;align-items:center;gap:18px;font-size:21px;font-weight:600">
    <svg width="22" height="20" viewBox="0 0 22 20"><path fill="#fff" d="M5 0h12v5H5zM1 6h20v9h-4v5H5v-5H1zm6 6v6h8v-6z"/></svg>Fax: 555-014-2291</div>
</section>

<section class="abs" style="top:2351px;left:0;width:1200px;height:754px">
  <h2 class="abs section-title" style="left:85px;top:76px;font-size:38px">Latest News</h2>
  <div class="abs rule" style="left:85px;top:135px"></div>
  <div class="abs poppins" style="left:1056px;top:125px;font-size:13px;font-weight:500;color:#111">VIEW ALL</div>
</section>
<article class="news-card" style="left:85px">
  <div class="ph" role="img" aria-label="Photo of a foot being bandaged" style="background:linear-gradient(180deg,#c5d2e0,#e9edf2)"></div>
  <div class="body"><h4>3 Tips To Prevent Diabetic Ulcers: When To Consider Hyperbaric Therapy</h4><div class="meta">Jan 20 - By Guest User</div><p>People with diabetes are more prone to infected wounds and diabetic ulcers. Hyperbaric therapy can help these infections heal faster.</p><div class="more">LEARN MORE <span>»</span></div></div>
</article>
<article class="news-card" style="left:437px">
  <div class="ph" role="img" aria-label="Photo of a patient resting in a hyperbaric chamber" style="background:linear-gradient(180deg,#cfd6dd,#eef0f2)"></div>
  <div class="body"><h4>Autism, Cerebral Palsy &amp; Fibromyalgia: 3 Lesser-Known Reasons To Consider HBOT</h4><div class="meta">Feb 13 - By Guest User</div><p>Hyperbaric oxygen therapy (HBOT) provides pure oxygen in a pressurized chamber, improving conditions such as autism, cerebral palsy, and fibromyalgia.</p><div class="more">LEARN MORE <span>»</span></div></div>
</article>
<article class="news-card" style="left:788px">
  <div class="ph" role="img" aria-label="Photo of a patient lying in a treatment bed" style="background:linear-gradient(180deg,#b9c3c8,#d9e2e4)"></div>
  <div class="body"><h4>How Many HBOT Sessions Do I Need? Treatment For Common Conditions</h4><div class="meta">Mar 18 - By Guest User</div><p>HBOT continues to be an effective means of treating a range of common health issues. However, each condition needs several sessions to heal effectively.</p><div class="more">LEARN MORE <span>»</span></div></div>
</article>

<footer class="abs site-footer">
  <div class="abs brand" style="left:85px;top:90px;color:#fff"><span class="dot"></span>BLUEGATE</div>
  <p class="abs" style="left:85px;top:168px;width:345px;font-size:13.5px;line-height:21px">Constantly looking for ways to evolve the treatment of wounds and provide services that add value to the providers who refer patients to our facilities.</p>
  <div class="abs social" style="left:85px;top:246px;gap:18px"><span style="width:16px;height:16px"></span><span style="width:16px;height:16px"></span><span style="width:16px;height:16px"></span><span style="width:16px;height:16px"></span></div>
  <div class="abs" style="left:463px;top:90px"><h4 class="poppins">Quick Links</h4>
    <ul class="foot-list"><li>Home</li><li>About</li><li>Blog</li><li>Contact</li><li>Privacy Policy</li></ul></div>
  <div class="abs" style="left:626px;top:90px"><h4 class="poppins">Opening Hours</h4>
    <ul class="foot-list"><li><span><b>Monday</b>: 8:00am - 5:00pm</span></li><li><span><b>Tuesday</b>: 8:00am - 5:00pm</span></li><li><span><b>Wednesday</b>: 8:00am - 5:00pm</span></li><li><span><b>Thursday</b>: 8:00am - 5:00pm</span></li><li><span><b>Friday</b>: 8:00am - 5:00pm</span></li></ul></div>
  <div class="abs" style="left:875px;top:90px;width:240px"><h4 class="poppins">Contact Details</h4>
    <ul class="foot-list contact-list"><li><span><b>Fairview:</b> 4820 Meadow Ridge Pkwy, Suite 210, Fairview, TX 75099</span></li><li><span><b>Westbrook:</b> 1275 Cedar Hollow Dr, Suite 105, Westbrook, TX 75101</span></li><li><span><b>Phone:</b> 555-014-2290</span></li><li><span><b>Fax:</b> 555-014-2291</span></li></ul></div>
  <div class="abs" style="left:85px;top:348px;width:1030px;height:1px;background:rgba(255,255,255,.2)"></div>
  <div class="abs poppins" style="left:0;top:376px;width:1200px;text-align:center;font-size:13px">© Copyright 2021 | All Rights Reserved | Powered by Northpeak Digital</div>
</footer>

</body>
</html>
```